Tilly the Otter - Kids (2-5years) - ALL NATURAL - Bath & Body Skincare - Label / Packaging Design

Carnwick Heather Estate is the owner of the 'celebrity' lavender bear, Tilly the Otter. Carnwick is the world largest commercial lavender farm and home to the world finest lavender, lavender oil and skincare products. www.carnwickheather-example.com

We are launching a line of Kids skincare products targeted to the Australian and China market (where Tilly is considered a superstar/celebrity).

All natural products made in Australia:

We are looking for 3-4 few packaging concept designs for packaging for our Tilly Kids - Bath, Body & Bed Range.

The "Tilly Kids" Toiletry Range includes:
= Shampoo/Bath Gel
= Fizzy Bath Bombs
= Moisturiser
= Pillow Spray (together aka the “Tilly Snoozetime Routine”)

= Later, possible additions to the Tilly the Otter range include the below items so the conceptual design must be adaptable.
- Bath robe
- Bed Linen Sets
- Crockey sets

See Filecrate folder here for all image and brand information:
https://www.filecrate-example.com/sh/8kqmvr2tw9x3hn1/QQpzrLmeTdFgYh7kWsVuXcA2b?dl=0

Note: There are some current DRAFT concept created by another designer in the image section of the brief. These are NOT ready or high quality enough (and too dull and busy) but will give you a good reference for what we don't want (too dark/busy/illegible). Please create new ideas....
Updates

HI - NEW FILECRATE FILE LINK IN CASE THE ONE I SENT PREVIOUSLY IS NOT WORKING - https://www.filecrate-example.com/sh/8kqmvr2tw9x3hn1/QQpzrLmeTdFgYh7kWsVuXcA2b?dl=0IVE ALSO ADDED A FEW NEW FILES... Added Wednesday, June 14, 2017

Pls see links to Penrick's and TOTs Organic... http://www.boxdesignshowcase-example.com/2017/02/tots-organic.html https://www.penricksorganic-example.com.au We asked our social media agency in china for their thoughts on the colour scheme's so far (not including new attempts here) and they said the following: "From our perspective - we agree that the colour hues are not quite right - and while we love Tilly, we wonder whether the current design and packaging options doesn't quite reflect the premium price points that you want to position these products. We are aware that you are limited with a certain number of packaging options but worry that the pale and purple colours may not attract Chinese parents. While sunscreen is not a premium product - please see the Chasing Wren package that one of our clients has had strong sales in China https://www.sunsafeshop-example.org.au/product/wren-splash-play-sunscreen.html In short, the Tilly design needs to be colourful, rich and vibrant in our opinion"

Target Market(s)

Children 2-5 years old. Primarily young Australian and Chinese mothers and their children.

Industry/Entity Type

Farm

Font styles to use
Other font styles liked:
• Topik px is the main wordmark font. The copy font is your choice.

Requirements
Must have
• Specifically, a general Packaging Design that can be used across a wide range of products and packaging types.
• Packaging & Visual Design –Important Considerations:
• Please be creative!
• •Please ensure the design can be used as a (waterproof) label or printed on the bottle...
• • Please show the design on various bottle sizes and colours (clear, white, cream etc)
• • Please suggest various eco-friendly bottle material (PBS free recyclable plastic)?
• • Must have multi-country / cultural appeal
• Must be polished, fun, western/australian design standard but also appeals to Chinese design tastes..
• Feel free to add some splashes of kid-friendly colours - blues, pinks, yellow, greens etc
• See Filecrate folder here for all image and brand information:
• https://www.filecrate-example.com/sh/8kqmvr2tw9x3hn1/QQpzrLmeTdFgYh7kWsVuXcA2b?dl=0
• Notes from our contracts manufacturer:
• "For the tube there will be limitation to the puck size, this is the opening diameter of the tube. On the tube you are not able to print 6mm from the top of the tube closure when printing. For sticker application on the tube you will need to allow for spacing on each edge to ensure there is no creasing"
• The current budget covers the overall concept and (and 1 x packaging completed) We are willing to negotiate an additional small cost for the extra 2-3 product specific designs.
• We expect print ready packaging and we will supply the dielines to the chosen designer once we have decided upon the exact size, style and approach for the packaging - printing or labels (this part might take a few weeks as we need to review our options) but we can release (part) payment before if required.
Should not have
• No brown-bottles please.

```html
<!DOCTYPE html>
<html lang="en">
<head>
<meta charset="utf-8">
<title>Tilly the Otter – Gel Shampoo Label</title>
<link rel="stylesheet" href="https://fonts.googleapis.com/css2?family=Patrick+Hand&family=Amatic+SC:wght@700&display=swap">
<style>
  :root {
    --canvas: #f4f4f2;
    --band: #8e67a3;
    --brand-purple: #8b5f9e;
    --panel: #ffffff;
    --check-blue: #a9cde4;
    --check-pink: #f1b7bd;
    --check-cream: #fbf8ea;
    --lavender-deep: #5c4a8a;
    --lavender-soft: #8b7ac2;
    --bear-light: #b79ae0;
    --bear-deep: #8463c0;
    --ink: #4a3f55;
    --green: #4f9a7d;
    --tan: #b88a5c;
    --teal: #3f8f8a;
  }
  html, body {
    margin: 0;
    width: 1200px;
    height: 849px;
    overflow: hidden;
    background: var(--canvas);
  }
  .label {
    position: absolute;
    left: 60px;
    top: 90px;
    width: 1080px;
    height: 668px;
    display: block;
  }
  .wordmark {
    font-family: "Patrick Hand", cursive;
    font-size: 34px;
    fill: var(--brand-purple);
  }
  .headline {
    font-family: "Patrick Hand", cursive;
    font-size: 64px;
  }
  .headline .c-green { fill: var(--green); }
  .headline .c-tan { fill: var(--tan); }
  .headline .c-teal { fill: var(--teal); }
  .product-name {
    font-family: "Amatic SC", sans-serif;
    font-weight: 700;
    font-size: 40px;
    letter-spacing: 3px;
    fill: var(--ink);
  }
  .net-weight {
    font-family: "Patrick Hand", cursive;
    font-size: 16px;
    fill: var(--ink);
  }
</style>
</head>
<body>
<svg class="label" viewBox="0 0 797 493" xmlns="http://www.w3.org/2000/svg">
  <defs>
    <linearGradient id="checkTone" x1="0" y1="0" x2="1" y2="1">
      <stop offset="0" stop-color="var(--check-blue)"/>
      <stop offset="0.45" stop-color="var(--check-cream)"/>
      <stop offset="0.75" stop-color="var(--check-pink)"/>
      <stop offset="1" stop-color="var(--check-blue)"/>
    </linearGradient>
    <linearGradient id="bearTone" x1="0" y1="0" x2="1" y2="1">
      <stop offset="0" stop-color="var(--bear-light)"/>
      <stop offset="1" stop-color="var(--bear-deep)"/>
    </linearGradient>
    <linearGradient id="sprigTone" x1="0" y1="0" x2="1" y2="0">
      <stop offset="0" stop-color="var(--lavender-soft)"/>
      <stop offset="1" stop-color="var(--lavender-deep)"/>
    </linearGradient>
  </defs>

  <rect class="label-background" x="0" y="0" width="797" height="493" fill="url(#checkTone)" opacity="0.75"
        role="img" aria-label="Soft blue, pink and cream gingham check pattern"/>

  <g class="white-cloud-panel" fill="var(--panel)">
    <circle cx="255" cy="110" r="95"/>
    <circle cx="320" cy="95" r="85"/>
    <circle cx="330" cy="240" r="150"/>
    <circle cx="270" cy="350" r="100"/>
    <circle cx="330" cy="390" r="100"/>
    <circle cx="410" cy="220" r="110"/>
  </g>

  <rect class="band band-top" x="0" y="0" width="797" height="18" fill="var(--band)"/>
  <rect class="band band-bottom" x="0" y="473" width="797" height="20" fill="var(--band)"/>

  <path class="bear-photo" d="M430 230 C 440 175, 520 160, 560 180 C 610 160, 700 170, 720 215 C 745 250, 740 300, 760 330 C 790 370, 797 420, 797 473 L 480 473 C 470 430, 430 420, 410 380 C 390 340, 400 290, 430 230 Z"
        fill="url(#bearTone)" role="img" aria-label="Photo of a plush purple lavender toy waving, with a ribbon at its neck"/>

  <g class="lavender-sprigs" fill="url(#sprigTone)">
    <rect x="215" y="35" width="90" height="14" rx="7" transform="rotate(35 260 42)" role="img" aria-label="Lavender sprig illustration"/>
    <rect x="195" y="255" width="90" height="14" rx="7" transform="rotate(-70 240 262)" role="img" aria-label="Lavender sprig illustration"/>
    <rect x="345" y="320" width="80" height="13" rx="6" transform="rotate(55 385 326)" role="img" aria-label="Lavender sprig illustration"/>
    <rect x="250" y="390" width="95" height="14" rx="7" transform="rotate(-20 297 397)" role="img" aria-label="Lavender sprig illustration"/>
  </g>

  <g class="brand-mark">
    <rect x="326" y="58" width="14" height="14" fill="var(--brand-purple)"/>
    <text class="wordmark" x="348" y="72">Tilly</text>
    <text class="wordmark" x="326" y="108">the Otter</text>
  </g>

  <text class="headline" x="215" y="222"><tspan class="c-green">Bath </tspan><tspan class="c-tan">time </tspan><tspan class="c-teal">fun!</tspan></text>

  <text class="product-name" x="200" y="366">GEL SHAMPOO</text>

  <text class="net-weight" x="330" y="443" text-anchor="middle">NET WEIGHT</text>
  <text class="net-weight" x="330" y="459" text-anchor="middle">12 OZ</text>
</svg>
</body>
</html>
```